Brightwater Subsea Systems Alliance

Hi, I am having a workshop at the beginning of June on the above topic and require the following:
I would like the following:
- PPT template in widescreen and regular format (these are really the same but just need but design just needs to be scalable). I like clean ppt templates showing the section but leaving much of the slide for actual content. I like clean no nonsense fonts (calibri, arial, etc)
- 3 fold brochure (stationary)
- poster template for 8.5"x11" and 11"x17" posters (stationary, I do not need a letterhead per se except for the workshop agenda.
- The added stationary and logo options I picked on the "Design Options" page should cover all of the above.

It is not for the https://tidewellhub.ca/ but we are an academic led network from www.halvardcol.ca wanting to do collaborate and do work in the key areas of the Tidewell Hub especially related to offshore oil and gas in the areas of: production optimization, automation, safety & risk, marine operations, communications and controls, human factors, remote leadership an teams.

Keywords: digital oilfield, offshore oil and gas, integrated operations, digitalization, TAX47, Ravnholt digital oil and gas, integrated operations, remote and harsh (ice and icebergs) offshore oil and gas field development, automation in oil and gas

I am hoping that since its just a workshop and the development needs to be done within the halvardcol.ca/pubrel/site/PKguide/ framework, so its really just a banner and/or the ppt/poster graphic can fit within the HVC Page Kit template. The creation we will do.

Giving an extension until tomorrow. Based on what I see now, we will need to work together a little bit to get what I want/need. Okay?

1 page

Serif
Sans Serif

3176b5
33a6d7
33b8a4

```html
<!DOCTYPE html>
<html lang="en">
<head>
<meta charset="utf-8">
<title>Marketing Plan</title>
<link rel="stylesheet" href="https://fonts.googleapis.com/css2?family=Montserrat:wght@600&family=Raleway:wght@300;400&family=Fira+Sans:wght@400;500&display=swap">
<style>
  :root {
    --blue: #3176b5;
    --slate: #4e5d79;
    --teal: #76d3c6;
    --teal-bar: #6fcfc4;
    --slate-bar: #56687f;
    --title-grey: #bdbdbd;
    --copy-grey: #9b9b9b;
    --caption-grey: #b3b3b3;
    --rule-grey: #a9a9a9;
    --white: #ffffff;
  }
  html, body {
    margin: 0;
    padding: 0;
    overflow: hidden;
    background: var(--white);
  }
  .slide {
    position: relative;
    width: 1200px;
    height: 900px;
    overflow: hidden;
    background: var(--white);
    font-family: "Fira Sans", Arial, sans-serif;
  }
  .top-bands {
    position: absolute;
    top: 0; left: 0;
    width: 1200px; height: 26px;
    display: flex;
  }
  .top-bands span { flex: 1; }
  .band-blue { background: var(--blue); }
  .band-teal { background: var(--teal-bar); }
  .band-slate { background: var(--slate-bar); }
  .slide-title {
    position: absolute;
    left: 35px; top: 58px;
    margin: 0;
    font-family: "Montserrat", Arial, sans-serif;
    font-weight: 600;
    font-size: 64px;
    letter-spacing: -1px;
    color: var(--title-grey);
  }
  .page-number {
    position: absolute;
    right: 43px; top: 74px;
    font-family: "Montserrat", Arial, sans-serif;
    font-weight: 600;
    font-size: 25px;
    letter-spacing: -0.5px;
    color: var(--title-grey);
  }
  .title-rule {
    position: absolute;
    left: 37px; top: 148px;
    width: 1123px;
    border-top: 2px dashed var(--rule-grey);
  }
  .intro {
    position: absolute;
    left: 37px; top: 171px;
    margin: 0;
    font-size: 19px;
    line-height: 27px;
    letter-spacing: 0.4px;
    color: var(--copy-grey);
  }
  .diagram {
    position: absolute;
    left: 0; top: 0;
  }
  .stat-value {
    font-family: "Raleway", Arial, sans-serif;
    font-weight: 300;
    font-size: 45px;
    fill: var(--white);
  }
  .stat-note {
    font-family: "Fira Sans", Arial, sans-serif;
    font-size: 17.5px;
    fill: var(--white);
  }
  .connector {
    fill: none;
    stroke: #8a8a8a;
    stroke-width: 1.6;
    stroke-dasharray: 7 6;
  }
  .headline {
    font-family: "Raleway", Arial, sans-serif;
    font-weight: 400;
    font-size: 33px;
  }
  .headline-blue { fill: var(--blue); }
  .headline-slate { fill: var(--slate); }
  .headline-teal { fill: var(--teal); }
  .caption {
    font-family: "Fira Sans", Arial, sans-serif;
    font-size: 15.5px;
    letter-spacing: 0.3px;
    fill: var(--caption-grey);
  }
</style>
</head>
<body>
<main class="slide">
  <div class="top-bands">
    <span class="band-blue"></span>
    <span class="band-teal"></span>
    <span class="band-slate"></span>
  </div>

  <h1 class="slide-title">MARKETING PLAN</h1>
  <div class="page-number">PAGE 1</div>
  <div class="title-rule"></div>

  <p class="intro">Lorem ipsum dolor sit amet, consectetur adipiscing elit, sed do eiusmod<br>tempor incididunt ut labore et dolore .</p>

  <svg class="diagram" width="1200" height="900" viewBox="0 0 1200 900">
    <!-- circles -->
    <circle cx="368" cy="451" r="188" fill="var(--blue)"/>
    <circle cx="837" cy="443" r="188" fill="var(--teal)"/>
    <circle cx="598" cy="443" r="188" fill="var(--slate)"/>

    <!-- icon areas -->
    <rect x="274" y="338" width="82" height="64" rx="6" fill="#ffffff" fill-opacity="0.18" role="img" aria-label="Line icon of an industrial refinery plant"/>
    <rect x="549" y="312" width="98" height="88" rx="6" fill="#ffffff" fill-opacity="0.18" role="img" aria-label="Line icon of an oil pump jack"/>
    <rect x="816" y="330" width="128" height="74" rx="6" fill="#ffffff" fill-opacity="0.2" role="img" aria-label="Line icon of a fuel tanker truck"/>

    <!-- stats -->
    <text class="stat-value" x="314" y="455" text-anchor="middle">30%</text>
    <text class="stat-note" x="314" y="485" text-anchor="middle">Lorem ipsum dolor</text>
    <text class="stat-note" x="314" y="510" text-anchor="middle">sit amet, consectetur.</text>

    <text class="stat-value" x="598" y="455" text-anchor="middle">30%</text>
    <text class="stat-note" x="598" y="487" text-anchor="middle">Lorem ipsum dolor</text>
    <text class="stat-note" x="598" y="512" text-anchor="middle">sit amet, consectetur.</text>

    <text class="stat-value" x="887" y="455" text-anchor="middle">30%</text>
    <text class="stat-note" x="887" y="485" text-anchor="middle">Lorem ipsum dolor</text>
    <text class="stat-note" x="887" y="510" text-anchor="middle">sit amet, consectetur.</text>

    <!-- connectors -->
    <path class="connector" d="M361 652 V690 Q361 707 344 707 H210 Q198 707 196 718"/>
    <path class="connector" d="M595 646 V722"/>
    <path class="connector" d="M847 648 V686 Q847 701 864 701 H1004 Q1012 701 1014 712"/>

    <!-- headlines -->
    <text class="headline headline-blue" x="185" y="778" text-anchor="middle">HEADLINE</text>
    <text class="caption" x="185" y="804" text-anchor="middle">Lorem ipsum dolor sit amet,</text>
    <text class="caption" x="185" y="825" text-anchor="middle">consectetur adipiscing elit,</text>
    <text class="caption" x="185" y="846" text-anchor="middle">sed do eiusmod tempor.</text>

    <text class="headline headline-slate" x="592" y="778" text-anchor="middle">HEADLINE</text>
    <text class="caption" x="592" y="804" text-anchor="middle">Lorem ipsum dolor sit amet,</text>
    <text class="caption" x="592" y="825" text-anchor="middle">consectetur adipiscing elit,</text>
    <text class="caption" x="592" y="846" text-anchor="middle">sed do eiusmod tempor.</text>

    <text class="headline headline-teal" x="1011" y="778" text-anchor="middle">HEADLINE</text>
    <text class="caption" x="1011" y="804" text-anchor="middle">Lorem ipsum dolor sit amet,</text>
    <text class="caption" x="1011" y="825" text-anchor="middle">consectetur adipiscing elit,</text>
    <text class="caption" x="1011" y="846" text-anchor="middle">sed do eiusmod tempor.</text>
  </svg>
</main>
</body>
</html>
```